Website Design For digital agency

We have an existing website called www.kwrp.co.uk which needs revamping. We are currently using the Duda web builder platform to build our website so we need someone to create or combine our existing pages into a user friends, modern design. We will need design assets for our internal team to implement. Here is a link to our support if you have any question regarding the the website builder or image sizes and available design widgets. https://help.tavelonix.com/hc/en-us/articles/480172650283-Image-Size-Guidelines

Target Market(s)

Small to medium businesses looking for revamps and new designs

Industry/Entity Type

Website

Number of Pages Required

5+ page

Font styles to use
Other font styles liked:
• Publica

Colors
33a6d7
3377b5
886aae

Requirements
Must have
• separate pages to outline the services we provide.

```html
<!DOCTYPE html>
<html lang="en">
<head>
<meta charset="utf-8">
<title>Kestrel Wave RipplePoint – Home and Services pages</title>
<link href="https://fonts.googleapis.com/css2?family=Poppins:wght@300;400;500;600;700;800&display=swap" rel="stylesheet">
<style>
:root{
  --bg-top:#06354f;
  --bg-bottom:#1aa3df;
  --blue:#0ea5ea;
  --blue-deep:#1c5f95;
  --band:#2493d9;
  --ink:#111418;
  --muted:#6b7580;
  --mint:#dff4f1;
  --white:#ffffff;
  --ghost:rgba(20,30,40,.035);
}
*{margin:0;padding:0;box-sizing:border-box}
html,body{width:837px;height:1200px;overflow:hidden}
body{font-family:"Poppins",sans-serif;color:var(--ink);background:linear-gradient(180deg,var(--bg-top) 0%,#0c5a82 40%,var(--bg-bottom) 100%);position:relative}
.board-label{position:absolute;top:22px;color:var(--white);font-weight:700;font-size:9.5px}
.page{position:absolute;top:61px;width:259px;background:var(--white);overflow:hidden;box-shadow:0 4px 14px rgba(0,0,0,.25)}
.page--home{left:134px;height:1073px}
.page--services{left:434px;height:1038px}
.page *{position:absolute}
.brand{display:flex;align-items:center;gap:2px;font-weight:800;font-size:4px;letter-spacing:.1px;top:11px;left:19px;white-space:nowrap}
.brand i{position:static;display:block;width:9px;height:9px;border-radius:50%;background:var(--ink)}
.nav{top:14px;left:110px;display:flex;gap:9px;font-size:2.6px;font-weight:500}
.nav b{position:static;font-weight:500}
.nav .active{color:var(--blue)}
.hdr-icon{top:11px;width:8px;height:8px;border-radius:50%}
.hdr-icon--phone{background:var(--blue)}
.hdr-icon--user{background:var(--white);border:.6px solid #ccd}
.hdr-icon svg{position:absolute;left:2px;top:2px;width:4px;height:4px}
.photo{background:linear-gradient(135deg,#7a8c99,#2f4656 60%,#1b8fcf)}
.photo--blue{background:linear-gradient(135deg,#37b2ea,#0e6fb0)}
.photo--warm{background:linear-gradient(135deg,#e9e3d8,#bfa682 55%,#6a7d8c)}
.h-sec{left:0;width:259px;text-align:center;font-weight:700;font-size:9px}
.desc{font-size:2.3px;line-height:4.2px;color:var(--muted)}
.center{left:0;width:259px;text-align:center}
.btn{font-size:2.3px;font-weight:600;border:.6px solid var(--blue);border-radius:6px;padding:1.3px 5px;color:var(--ink);background:var(--white);white-space:nowrap}
.btn--solid{background:var(--blue);color:var(--white);border-color:var(--blue)}
.card{width:67px;height:73px;background:var(--white);border-radius:2px;box-shadow:0 2px 6px rgba(20,60,90,.1);text-align:center}
.card--on{background:var(--blue);color:var(--white)}
.card .ic{left:24px;top:12px;width:18px;height:18px;border-radius:50%;background:var(--blue);border:1.6px solid #bfe6fa}
.card--on .ic{background:var(--white);border-color:#7fd0f5}
.card .ic i{left:5px;top:4.5px;width:5px;height:6px;border:.6px solid var(--white);border-radius:1px}
.card--on .ic i{border-color:var(--blue)}
.card h4{top:40px;left:0;width:67px;font-size:3px;font-weight:600}
.card p{top:49px;left:7px;width:53px;font-size:2.2px;line-height:4px;color:var(--muted)}
.card--on p{color:#e6f6ff}
.ghost{font-weight:800;color:var(--ghost);white-space:nowrap;line-height:1}
.title{font-weight:700;font-size:9px;line-height:11px}
.kicker{font-size:2.8px;color:var(--blue);font-weight:500}
.post{width:62px}
.post .img{left:0;top:0;width:62px;height:50px}
.post .bar{left:0;top:50px;width:62px;height:7px;background:var(--blue);color:var(--white);font-size:1.9px;display:flex;align-items:center;gap:8px;padding-left:4px}
.post .bar b{position:static;font-weight:400}
.post h5{top:66px;left:1px;font-size:3px;font-weight:600;white-space:nowrap}
.post p{top:74px;left:1px;width:60px;font-size:2.1px;line-height:4px;color:var(--muted)}
.post .btn{top:95px;left:1px}
.blob{border-radius:58% 42% 55% 45%/48% 58% 42% 52%}
.mint{background:var(--mint)}
.contact{left:0;width:259px;height:108px;overflow:hidden;background:linear-gradient(120deg,#1a8ad3,#32b0ee 50%,#1580c9)}
.contact .hole{left:62px;top:2px;width:145px;height:104px;background:var(--blue-deep);border-radius:48% 52% 46% 54%/52% 44% 56% 48%}
.contact .lead{left:0;width:259px;text-align:center;font-size:2.2px;color:var(--white)}
.contact h3{left:0;width:259px;text-align:center;font-size:9px;font-weight:700;color:var(--white)}
.field{background:var(--white);border-radius:3px;height:7.5px;width:44px;font-size:1.9px;color:#9aa;padding:2.5px 0 0 5px}
.field--msg{width:92px;height:18px;border-radius:4px}
.contact .send{font-size:2px;font-weight:600;color:var(--white);border:.6px solid var(--white);border-radius:5px;padding:1.3px 4px;background:var(--blue-deep);white-space:nowrap}
.foot-h{font-size:3px;font-weight:600}
.foot-t{font-size:2.2px;line-height:4.1px;color:var(--muted)}
.foot-list{font-size:2.2px;line-height:5.6px;color:var(--muted)}
.foot-list span{display:block;position:static}
.mail-in{width:59px;height:7px;border:.6px solid var(--blue);border-radius:4px;font-size:2px;color:#9aa;padding:2px 0 0 4px}
.mail-in i{right:1px;top:.8px;width:4.6px;height:4.6px;border-radius:50%;background:var(--ink)}
.dot{width:4px;height:4px;border-radius:50%;background:var(--ink)}
.pin{width:3px;height:3px;border-radius:50% 50% 50% 0;transform:rotate(-45deg);background:var(--blue)}
.rule{height:.5px;background:#e3e7ea}
.copy{left:0;width:259px;text-align:center;font-size:2.1px;line-height:4.8px;color:var(--muted)}
.hero-band{left:0;top:28px;width:259px;height:65px;background:var(--blue);overflow:hidden}
.hero-band .swirl{background:rgba(255,255,255,.08)}
</style>
</head>
<body>

<div class="board-label" style="left:134px">Home Page</div>
<div class="board-label" style="left:434px">Services Page</div>

<!-- ============ HOME PAGE ============ -->
<main class="page page--home">
  <div class="brand"><i></i>KESTREL WAVE</div>
  <div class="blob" style="left:92px;top:-6px;width:172px;height:150px;border:3px solid #cdeefb;border-radius:50% 50% 48% 52%/42% 45% 55% 58%"></div>
  <div class="photo" role="img" aria-label="Woman thinking at a desk in front of a computer monitor" style="left:97px;top:-4px;width:166px;height:144px;border-radius:50% 50% 48% 52%/42% 45% 55% 58%"></div>
  <div class="blob" style="left:150px;top:110px;width:115px;height:36px;border-bottom:2.4px solid var(--blue);border-radius:0 0 60% 50%"></div>
  <nav class="nav"><b class="active">Home</b><b>About Us</b><b>Services</b><b>Blog</b><b>Contact</b></nav>
  <div class="hdr-icon hdr-icon--phone" style="left:212px"><svg viewBox="0 0 10 10"><path d="M2 1l2 2-1 1.3q1 2 2.7 2.7L7 6l2 2-1.3 1.2Q3 9 1 2.3z" fill="#fff"/></svg></div>
  <div class="hdr-icon hdr-icon--user" style="left:222px"><svg viewBox="0 0 10 10"><circle cx="5" cy="3.3" r="2" fill="none" stroke="#333"/><path d="M1.5 9q3.5-5 7 0" fill="none" stroke="#333"/></svg></div>

  <div style="left:20px;top:47px;font-size:8.4px;font-weight:300">Kestrel Wave</div>
  <div style="left:20px;top:58px;font-size:15.5px;font-weight:800">RipplePoint</div>
  <p class="desc" style="left:20px;top:80px;width:60px">We tidy every corner of your site, and we provide you</p>
  <div class="btn btn--solid" style="left:20px;top:97px">Get A Quote</div>

  <div class="blob mint" style="left:235px;top:250px;width:40px;height:90px;opacity:.6"></div>
  <div class="h-sec" style="top:172px">SOME OF OUR SERVICES</div>
  <p class="desc center" style="top:188px;padding:0 58px">We tidy every corner of your site, and we provide you with the full range of digital marketing services, everything from website &amp; traffic building to social media campaign construction.</p>

  <div class="card" style="left:21px;top:209px"><div class="ic"><i></i></div><h4>Social Media</h4><p>Contrary to popular belief, our posts are never just random text.</p></div>
  <div class="card card--on" style="left:97px;top:209px"><div class="ic"><i></i></div><h4>Press Release</h4><p>Contrary to popular belief, our posts are never just random text.</p></div>
  <div class="card" style="left:172px;top:209px"><div class="ic"><i></i></div><h4>SEO</h4><p>Contrary to popular belief, our posts are never just random text.</p></div>
  <div class="card" style="left:21px;top:290px"><div class="ic"><i></i></div><h4>Blog writing</h4><p>Contrary to popular belief, our posts are never just random text.</p></div>
  <div class="card" style="left:97px;top:290px"><div class="ic"><i></i></div><h4>Web services</h4><p>Contrary to popular belief, our posts are never just random text.</p></div>
  <div class="card" style="left:172px;top:290px"><div class="ic"><i></i></div><h4>Graphic Design</h4><p>Contrary to popular belief, our posts are never just random text.</p></div>

  <div class="ghost" style="left:120px;top:400px;font-size:32px">ABOUT</div>
  <div class="photo photo--blue" role="img" aria-label="Woman working at a laptop in a bright office" style="left:-8px;top:394px;width:120px;height:124px;border-radius:20% 80% 45% 55%/30% 50% 50% 70%"></div>
  <div class="title" style="left:131px;top:435px">ABOUT US</div>
  <div class="kicker" style="left:131px;top:450px">Who We Are</div>
  <p class="desc" style="left:131px;top:458px;width:95px">We design clear, modern websites for growing small businesses and keep them running well. Every page we build is planned around your customers, so visitors find what they need quickly and come back again.</p>
  <div class="btn" style="left:131px;top:481px">View More</div>

  <div class="blob mint" style="left:-30px;top:690px;width:80px;height:160px;opacity:.7"></div>
  <div class="blob mint" style="left:203px;top:800px;width:52px;height:42px"></div>
  <div class="blob mint" style="left:180px;top:778px;width:16px;height:16px;border-radius:50%"></div>

  <div class="h-sec" style="top:526px">RECENT BLOG POSTS</div>
  <p class="desc center" style="top:542px;padding:0 58px">We tidy every corner of your site, and we provide you with the full range of digital marketing services, everything from website &amp; traffic building to social media campaign construction.</p>

  <article class="post" style="left:33px;top:566px;height:110px">
    <div class="img photo--warm" role="img" aria-label="Woman writing notes at a desk"></div>
    <div class="bar"><b>2 Comments</b><b>By Tobias</b></div>
    <h5>Office Supply Picks</h5>
    <p>Contrary to popular belief, this post is not simply random text. It has roots in a piece of classical Latin</p>
    <div class="btn">View More</div>
  </article>
  <article class="post" style="left:101px;top:566px;height:110px">
    <div class="img photo--blue" role="img" aria-label="Team reviewing charts on a tablet"></div>
    <div class="bar"><b>2 Comments</b><b>By Tobias</b></div>
    <h5>Impact of Technology</h5>
    <p>Contrary to popular belief, this post is not simply random text. It has roots in a piece of classical Latin</p>
    <div class="btn">View More</div>
  </article>
  <article class="post" style="left:169px;top:566px;height:110px">
    <div class="img photo" role="img" aria-label="Hands pointing at a laptop screen"></div>
    <div class="bar"><b>2 Comments</b><b>By Tobias</b></div>
    <h5>Company Laptop for Personal</h5>
    <p>Contrary to popular belief, this post is not simply random text. It has roots in a piece of classical Latin</p>
    <div class="btn">View More</div>
  </article>

  <div class="kicker center" style="top:717px">Testimonials</div>
  <div class="h-sec" style="top:723px">WHAT OUR CLIENT’S SAY</div>
  <div class="center" style="top:741px;font-size:12px;font-weight:800;color:var(--blue)">“</div>
  <p class="desc center" style="top:757px;padding:0 65px">They rebuilt our whole site in a few weeks and the new pages are clear, quick and easy to update. Our enquiries have grown every month since the launch, and the team answer questions fast.</p>
  <div class="photo--blue" role="img" aria-label="Portrait of the customer" style="left:120px;top:779px;width:20px;height:20px;border-radius:50%"></div>
  <div class="center" style="top:806px;font-size:3px;font-weight:600">Marcus Ellery</div>
  <div class="center" style="top:811px;font-size:2.1px;color:var(--muted)">Customer</div>

  <section class="contact" style="top:855px">
    <div class="hole"></div>
    <div class="lead" style="top:16px">Contrary to popular belief, Lorem</div>
    <h3 style="top:20px">CONTACT US</h3>
    <div class="field" style="left:85px;top:37px">First Name</div>
    <div class="field" style="left:133px;top:37px">Last Name</div>
    <div class="field" style="left:85px;top:50px">Email address</div>
    <div class="field" style="left:133px;top:50px">Phone</div>
    <div class="field field--msg" style="left:85px;top:63px">Message</div>
    <div class="send" style="left:116px;top:88px">Send Message</div>
  </section>

  <div class="brand" style="top:983px;left:22px"><i></i>KESTREL WAVE</div>
  <p class="foot-t" style="left:22px;top:999px;width:60px">We build clear, modern websites that help small firms grow and win new customers online.</p>
  <div class="mail-in" style="left:21px;top:1019px">Email address<i></i></div>
  <div class="foot-h" style="left:115px;top:986px">Let’s Connect</div>
  <div class="foot-list" style="left:115px;top:998px"><span>About</span><span>Website Development &amp; Hosting</span><span>SEO &amp; Content management</span><span>Search Ad Management</span><span>Social Media Marketing</span><span>Website Resources</span></div>
  <div class="foot-h" style="left:185px;top:986px">Contact Us</div>
  <div class="pin" style="left:185px;top:1000px"></div>
  <p class="foot-t" style="left:191px;top:998px;width:50px">Address: Hartwell Hub, 14 Linden Row, London, EC2A 9QT</p>
  <p class="foot-t" style="left:191px;top:1011px;color:var(--blue)">info@kwrp.co.uk</p>
  <div class="dot" style="left:185px;top:1023px"></div>
  <div class="dot" style="left:191px;top:1023px"></div>
  <div class="rule" style="left:20px;top:1044px;width:219px"></div>
  <p class="copy" style="top:1051px">© Copyright 2021 Kestrel Wave Ltd trading as Kestrel Wave RipplePoint. Registered in<br>England and Wales. Registered Number: 04417326. Privacy Policy</p>
</main>

<!-- ============ SERVICES PAGE ============ -->
<main class="page page--services">
  <div class="brand"><i></i>KESTREL WAVE</div>
  <nav class="nav" style="gap:10px"><b>Home</b><b>About Us</b><b class="active">Services</b><b>Blog</b><b>Contact</b></nav>
  <div class="hdr-icon hdr-icon--phone" style="left:211px"><svg viewBox="0 0 10 10"><path d="M2 1l2 2-1 1.3q1 2 2.7 2.7L7 6l2 2-1.3 1.2Q3 9 1 2.3z" fill="#fff"/></svg></div>
  <div class="hdr-icon hdr-icon--user" style="left:221px"><svg viewBox="0 0 10 10"><circle cx="5" cy="3.3" r="2" fill="none" stroke="#333"/><path d="M1.5 9q3.5-5 7 0" fill="none" stroke="#333"/></svg></div>

  <section class="hero-band">
    <div class="swirl blob" style="left:60px;top:-20px;width:150px;height:110px"></div>
    <div class="swirl blob" style="left:200px;top:-30px;width:80px;height:60px"></div>
    <div style="left:0;width:259px;text-align:center;top:22px;font-size:15px;font-weight:800;color:var(--white)">Services</div>
    <div style="left:0;width:259px;text-align:center;top:42px;font-size:2.3px;font-weight:600;color:var(--white)">Home &nbsp;→&nbsp; Services</div>
  </section>

  <div class="ghost" style="left:131px;top:116px;font-size:32px">WEB</div>
  <div class="photo" role="img" aria-label="Person using a phone over a laptop keyboard" style="left:-6px;top:114px;width:126px;height:116px;border-radius:35% 65% 50% 50%/30% 45% 55% 70%;border:2px solid var(--blue)"></div>
  <div class="title" style="left:141px;top:149px">WEBSITE<br>DEVELOPMENT<br>&amp; HOSTING</div>
  <div class="kicker" style="left:141px;top:185px">Web Services</div>
  <p class="desc" style="left:141px;top:193px;width:92px">Providing small to medium sized businesses with a full range of web services including high quality custom website design, website development and search marketing services.</p>
  <div class="btn" style="left:141px;top:216px">View More</div>

  <div class="blob mint" style="left:-20px;top:265px;width:48px;height:90px;opacity:.7"></div>
  <div class="ghost" style="left:31px;top:252px;font-size:32px">SEO</div>
  <div class="title" style="left:36px;top:286px">SEO/CONTENT<br>MANAGEMENT</div>
  <div class="kicker" style="left:36px;top:310px">SEO</div>
  <p class="desc" style="left:36px;top:319px;width:95px">Good content &amp; SEO are important aspects in making your website easy for both users and search engines to understand. Although search engines have become increasingly clever, they still can't see a page the same way a human can.</p>
  <div class="btn" style="left:36px;top:347px">View More</div>
  <div class="photo--blue" role="img" aria-label="Smiling woman talking on a phone" style="left:149px;top:268px;width:115px;height:104px;border-radius:30% 70% 55% 45%/40% 30% 70% 60%"></div>
  <div style="left:204px;top:254px;width:16px;height:16px;border-radius:50%;background:var(--blue)"></div>
  <div style="left:228px;top:246px;width:30px;height:12px;border-radius:50%;background:var(--blue);transform:rotate(-35deg)"></div>

  <div class="ghost" style="left:2px;top:386px;font-size:32px">SOCIAL MEDIA</div>
  <div class="photo" role="img" aria-label="Man working at a laptop in an office" style="left:-6px;top:409px;width:123px;height:103px;border-radius:40% 60% 55% 45%/35% 45% 55% 65%"></div>
  <div style="left:58px;top:403px;width:26px;height:18px;border-radius:50%;background:#6f8791"></div>
  <div class="title" style="left:139px;top:434px">SOCIAL MEDIA<br>MARKETING</div>
  <div class="kicker" style="left:139px;top:459px">Social Media</div>
  <p class="desc" style="left:139px;top:469px;width:56px">Need to reach new customers? Our social media management will enable your company to reach thousands of potential new customers online.</p>
  <div class="btn" style="left:139px;top:495px">View More</div>

  <div class="ghost" style="left:31px;top:533px;font-size:32px">EMAIL</div>
  <div class="title" style="left:36px;top:565px">EMAIL<br>MARKETING</div>
  <div class="kicker" style="left:36px;top:590px">Marketing</div>
  <p class="desc" style="left:36px;top:599px;width:95px">Email outperforms other marketing strategies, earning £32 for every £1 spent on average. It's the most cost-effective way to gain new clients and keep existing ones coming back.</p>
  <div class="btn" style="left:36px;top:621px">View More</div>
  <div class="photo--warm" role="img" aria-label="Woman on a phone call at a laptop" style="left:154px;top:527px;width:110px;height:115px;border-radius:55% 45% 40% 60%/40% 35% 65% 60%;border:2px solid var(--blue)"></div>

  <div class="ghost" style="left:73px;top:660px;font-size:32px">BRANDING</div>
  <div class="photo--warm" role="img" aria-label="Hands arranging paper icons on a wooden table" style="left:-10px;top:652px;width:89px;height:140px;border-radius:0 70% 60% 0/0 50% 60% 0"></div>
  <div class="title" style="left:100px;top:697px">BRANDING</div>
  <div class="kicker" style="left:100px;top:710px">Growth</div>
  <p class="desc" style="left:100px;top:719px;width:125px">Great branding is a key factor when trying to attract customers to your new or growing business. Our branding specialist will enable your company to stand out from the crowd &amp; thousands of potential new customers online.</p>
  <div class="btn" style="left:100px;top:739px">Coming Soon</div>
  <div class="mint" style="left:181px;top:753px;width:16px;height:16px;border-radius:50%"></div>
  <div class="blob mint" style="left:203px;top:757px;width:52px;height:42px"></div>
  <div class="blob mint" style="left:225px;top:430px;width:50px;height:120px;opacity:.35"></div>

  <section class="contact" style="top:821px">
    <div class="hole"></div>
    <div class="lead" style="top:16px">Contrary to popular belief, Lorem</div>
    <h3 style="top:20px">CONTACT US</h3>
    <div class="field" style="left:85px;top:37px">First Name</div>
    <div class="field" style="left:133px;top:37px">Last Name</div>
    <div class="field" style="left:85px;top:50px">Email address</div>
    <div class="field" style="left:133px;top:50px">Phone</div>
    <div class="field field--msg" style="left:85px;top:63px">Message</div>
    <div class="send" style="left:116px;top:88px">Send Message</div>
  </section>

  <div class="brand" style="top:952px;left:22px"><i></i>KESTREL WAVE</div>
  <p class="foot-t" style="left:22px;top:967px;width:60px">We build clear, modern websites that help small firms grow and win new customers online.</p>
  <div class="mail-in" style="left:21px;top:987px">Email address<i></i></div>
  <div class="foot-h" style="left:115px;top:953px">Let’s Connect</div>
  <div class="foot-list" style="left:115px;top:965px"><span>About</span><span>Website Development &amp; Hosting</span><span>SEO &amp; Content management</span><span>Search Ad Management</span><span>Social Media Marketing</span><span>Website Resources</span></div>
  <div class="foot-h" style="left:185px;top:953px">Contact Us</div>
  <div class="pin" style="left:185px;top:967px"></div>
  <p class="foot-t" style="left:191px;top:965px;width:50px">Address: Hartwell Hub, 14 Linden Row, London, EC2A 9QT</p>
  <p class="foot-t" style="left:191px;top:978px;color:var(--blue)">info@kwrp.co.uk</p>
  <div class="dot" style="left:185px;top:990px"></div>
  <div class="dot" style="left:191px;top:990px"></div>
  <div class="rule" style="left:20px;top:1009px;width:219px"></div>
  <p class="copy" style="top:1016px">© Copyright 2021 Kestrel Wave Ltd trading as Kestrel Wave RipplePoint. Registered in<br>England and Wales. Registered Number: 04417326. Privacy Policy</p>
</main>

</body>
</html>
```